New Website Announcement

We need a flyer to announce our new website to customers and prospective clients. The website will be launching soon, but I can provide a detailed outline in PDF form with copy and imagery to serve as inspiration for this design.

I would like a postcard size document that can be mailed in an envelope (no need for postcard style mailer info on 1 side)

About my company:

Clearwater Lantern Group is a new breed of marketing consulting agency built for the next frontier of consumer learning. Social interaction will be at the heart of great insights going forward – in how consumers engage with brands and in how organizations socialize what they learn to gain competitive advantage.
By fusing innovative insights techniques, technology and compelling graphic design-based reporting, we ensure results get noticed and make an impact.

contact info that can also be included:

Email: morgan@clearwater-lantern.com

Phone: 518-732-6148

New High Res logo file has been added. (.ai)

Thanks

Reason: Giving more time next week for submissions. This project has been committed. Thanks !

Attention all designers submitting a design for this project. Please keep in mind a few important details about this project.

1. Remember that the main objective of this postcard is to announce my new website.

2. Please be sure to read the brief for the copy I would like on each side. You can be creative in how it is displayed, but I need this key information somewhere. All other copy on the attached files is for your background only.

3. Please do not submit overly simple designs that just take the images I provided and overlay a text box with my copy. I could easily do this myself in PowerPoint in 5 minutes.

4. Remember that the design should be edgy and modern but needs to be professional and speak to a business audience.

Please submit any questions. Thank you for your submissions. 

Morgan

Illustrator high res logo file now correctly uploaded. Thanks.

Target Market(s)

senior level marketing and research clients at large companies and agencies

Industry/Entity Type

Marketing

Requirements
Must have
• Main message:

Need an engaging way to tell customers and prospective clients that we have a new website and that they should come visit us online to learn more about out services, check out case studies and read about our exciting partnerships.

COPY TO USE - UPDATED

Side 1:
(logo)
Introducing Clearwater Lantern Group

Let’s talk about taking research out of the dark ages.

Visit our newly launched website to learn how and get in touch.

www.clearwater-lantern.com

Side 2
Logo
followed by tagline:
Consumer insights that get noticed.
A leading-edge marketing partnership that really works.

Additional text to use on Side 2:
How we can help...

Think of us as your go-to resource for identifying and incorporating the most innovative and exciting techniques into your research programs. We carefully curate and develop close partnerships with the best of the best - from online qualitative research and mobile ethnography to social media listening and fresh takes on concept testing, we can guide the way.

Plus, we believe that socializing consumer learning is just as critical as gathering it.By taking insights deliverables to the next level – through infographics, videos, magazines,interactive profiles and so much more – we are getting stakeholders excited to engage with research and inspired to take action because of it.
It’s a new way to look at insights from a new type of partner. And, it’s a new way to get the most from your research dollars.
Nice to have
• could incorporate our website main image of the lamp on white brick background which is attached, but not 100% mandatory.
Should not have
• - should not be too playful or young, but needs to be modern and design focused

- should not be cluttered or overly 'salesy'

- needs to be upscale and elegant / compelling and aligned with the look and feel of the website imagery (see attached)

```html
<!DOCTYPE html>
<html lang="en">
<head>
<meta charset="utf-8">
<title>Clearwater Lantern Group – Website Launch Postcard</title>
<link rel="stylesheet" href="https://fonts.googleapis.com/css2?family=Bodoni+Moda:ital,wght@0,400;1,700&family=Playfair+Display:ital,wght@1,700&family=Questrial&family=Roboto+Condensed:ital,wght@1,300&display=swap">
<style>
  :root{
    --stage:#000;
    --ink-white:#fff;
    --brand-blue:#1f78c8;
    --deep-blue:#24398f;
    --mid-blue:#1a8fdc;
    --pale-blue:#e9f5fc;
    --brick-light:#eeeeee;
    --brick-mid:#b9b9b9;
    --text-dark:#1b1b1b;
  }
  *{margin:0;padding:0;box-sizing:border-box}
  html,body{width:1000px;height:1200px;overflow:hidden;background:var(--stage)}
  .canvas{position:relative;width:1000px;height:1200px}
  .side-label{position:absolute;color:var(--ink-white);font:italic 300 58px "Roboto Condensed",sans-serif}
  .side-label--front{left:24px;top:208px}
  .side-label--back{left:872px;top:880px}
  .card{position:absolute;left:158px;width:695px;height:538px;overflow:hidden;border:1px solid #555}
  .card--front{top:43px}
  .card--back{top:622px}
  .card-art{position:absolute;left:0;top:0;width:695px;height:538px}
  .abs{position:absolute}

  /* front */
  .intro{left:187px;top:206px;font:italic 700 15px "Playfair Display",serif;color:var(--text-dark)}
  .wordmark{font:400 30px/1.05 "Questrial",sans-serif;color:var(--brand-blue);letter-spacing:.5px}
  .wordmark--front{left:187px;top:228px}
  .headline{right:18px;top:214px;text-align:right;font:italic 700 26px/1.3 "Playfair Display",serif;color:var(--ink-white)}
  .headline .small{font-size:21px}
  .headline .large{font-size:28px}
  .visit{right:16px;top:396px;text-align:right;font:italic 400 22px/1.35 "Questrial",sans-serif;color:var(--ink-white)}
  .visit .l2{font-size:24px}
  .web{right:16px;top:480px;display:flex;align-items:center;gap:10px;font:italic 700 30px "Questrial",sans-serif;color:var(--ink-white)}

  /* back */
  .tagline{left:241px;top:60px;font:italic 700 14px "Playfair Display",serif;color:var(--text-dark)}
  .tagline small{display:block;font-size:8px;margin-top:3px}
  .wordmark--back{right:18px;top:20px;text-align:right}
  .help-title{left:22px;top:140px;font:italic 700 14px "Playfair Display",serif;color:var(--ink-white)}
  .help-copy{left:23px;top:181px;font:400 11.5px/19px "Bodoni Moda",serif;color:var(--ink-white)}
  .story{right:27px;top:180px;font:400 18px/20px "Bodoni Moda",serif;color:var(--brand-blue);text-align:right}
  .line{display:block;white-space:nowrap}
  .line--fit{width:var(--w);text-align:justify;text-align-last:justify}
  .story .line--fit{margin-left:auto}
  .contact-bar{left:0;top:495px;width:695px;height:43px;background:var(--ink-white);font:400 16px "Bodoni Moda",serif;color:var(--brand-blue)}
  .contact{display:flex;align-items:center;gap:10px;position:absolute;top:10px}
  .contact--email{left:84px}
  .contact--phone{left:470px}
</style>
</head>
<body>
<div class="canvas">
  <div class="side-label side-label--front">Front</div>
  <div class="side-label side-label--back">Back</div>

  <!-- FRONT -->
  <section class="card card--front">
    <svg class="card-art" viewBox="0 0 695 538">
      <defs>
        <linearGradient id="frontBlue" x1="1" y1="0" x2="0.45" y2="1">
          <stop offset="0" stop-color="var(--pale-blue)"/>
          <stop offset="0.3" stop-color="var(--mid-blue)"/>
          <stop offset="0.7" stop-color="var(--deep-blue)"/>
          <stop offset="1" stop-color="var(--deep-blue)"/>
        </linearGradient>
        <radialGradient id="frontWall" cx="0.45" cy="0.4" r="0.7">
          <stop offset="0" stop-color="var(--brick-light)"/>
          <stop offset="1" stop-color="var(--brick-mid)"/>
        </radialGradient>
      </defs>
      <rect width="695" height="538" fill="url(#frontBlue)"/>
      <path d="M0,0 L420,0 C480,60 490,190 440,290 C380,400 230,455 0,455 Z" fill="url(#frontWall)" role="img" aria-label="Photo of an arc floor lamp glowing against a white brick wall"/>
      <path d="M420,0 C480,60 490,190 440,290 C380,400 230,455 0,455" fill="none" stroke="#fff" stroke-width="9"/>
    </svg>
    <div class="abs intro">Introducing...</div>
    <div class="abs wordmark wordmark--front">Clearwater<br>Lantern Group</div>
    <div class="abs headline">Let’s talk about<br><span class="small">taking research out</span><br><span class="large">of the dark ages.</span></div>
    <div class="abs visit">Visit our newly launched website<br><span class="l2">to learn how and get in touch.</span></div>
    <div class="abs web">
      <svg width="32" height="32" viewBox="0 0 32 32" aria-hidden="true"><circle cx="16" cy="16" r="14" fill="none" stroke="#fff" stroke-width="2.5"/><ellipse cx="16" cy="16" rx="6" ry="14" fill="none" stroke="#fff" stroke-width="2"/><line x1="2" y1="16" x2="30" y2="16" stroke="#fff" stroke-width="2"/></svg>
      <span>www.clearwater-lantern.com</span>
    </div>
  </section>

  <!-- BACK -->
  <section class="card card--back">
    <svg class="card-art" viewBox="0 0 695 538">
      <defs>
        <linearGradient id="backBlue" x1="0" y1="0" x2="0.5" y2="1">
          <stop offset="0" stop-color="var(--pale-blue)"/>
          <stop offset="0.3" stop-color="var(--mid-blue)"/>
          <stop offset="0.75" stop-color="var(--deep-blue)"/>
          <stop offset="1" stop-color="var(--deep-blue)"/>
        </linearGradient>
        <linearGradient id="backWall" x1="0" y1="0" x2="0" y2="1">
          <stop offset="0" stop-color="var(--brick-light)"/>
          <stop offset="1" stop-color="var(--brick-mid)"/>
        </linearGradient>
        <clipPath id="wallClip"><path d="M287,0 C240,40 205,130 213,200 C225,300 330,410 480,440 C560,455 640,458 695,460 L695,0 Z"/></clipPath>
      </defs>
      <rect width="695" height="538" fill="url(#backBlue)"/>
      <path d="M287,0 C240,40 205,130 213,200 C225,300 330,410 480,440 C560,455 640,458 695,460 L695,0 Z" fill="url(#backWall)" role="img" aria-label="Photo of a white brick wall"/>
      <rect x="0" y="178" width="695" height="230" fill="#fff" clip-path="url(#wallClip)"/>
      <path d="M287,0 C240,40 205,130 213,200 C225,300 330,410 480,440 C560,455 640,458 695,460" fill="none" stroke="#fff" stroke-width="9"/>
    </svg>
    <div class="abs tagline">Consumer insights that get noticed.<small>A leading-edge marketing partnership that really works.</small></div>
    <div class="abs wordmark wordmark--back">Clearwater<br>Lantern Group</div>
    <div class="abs help-title">How we can help...</div>
    <p class="abs help-copy">
      <span class="line line--fit" style="--w:161px">Think of us as your go-to</span>
      <span class="line line--fit" style="--w:164px">resource for identifying</span>
      <span class="line line--fit" style="--w:166px">and incorporating the</span>
      <span class="line line--fit" style="--w:171px">most innovative and excit-</span>
      <span class="line line--fit" style="--w:179px">ing techniques into your</span>
      <span class="line line--fit" style="--w:189px">research programs. We care-</span>
      <span class="line line--fit" style="--w:191px">fully curate and develop close</span>
      <span class="line line--fit" style="--w:216px">partnerships with the best of the</span>
      <span class="line line--fit" style="--w:229px">best - from online qualitative</span>
      <span class="line line--fit" style="--w:247px">research and mobile ethnography to</span>
      <span class="line line--fit" style="--w:269px">social media listening and fresh takes on</span>
      <span class="line">concept testing, we can guide the way.</span>
    </p>
    <p class="abs story">
      <span class="line line--fit" style="--w:433px">Plus, we believe that socializing consumer learn-</span>
      <span class="line line--fit" style="--w:440px">ing is just as critical as gathering it. By taking in-</span>
      <span class="line line--fit" style="--w:428px">sights deliverables to the next level – through in-</span>
      <span class="line line--fit" style="--w:416px">fographics, videos, magazines, interactive pro-</span>
      <span class="line line--fit" style="--w:401px">files and so much more – we are getting stake-</span>
      <span class="line line--fit" style="--w:386px">holders excited to engage with research and</span>
      <span class="line">inspired to take action because of it.</span>
      <span class="line">It’s a new way to look at insights from a</span>
      <span class="line">new type of partner. And, it’s a new</span>
      <span class="line">way to get the most from your re-</span>
      <span class="line">search dollars.</span>
    </p>
    <div class="abs contact-bar">
      <div class="contact contact--email">
        <svg width="22" height="22" viewBox="0 0 22 22" aria-hidden="true"><circle cx="11" cy="11" r="11" fill="var(--brand-blue)"/><path d="M7,5 L9.5,5 L10.5,8 L9,9.3 C9.8,11 11,12.2 12.7,13 L14,11.5 L17,12.5 L17,15 C12,16 6,10 7,5 Z" fill="#fff"/></svg>
        <span>morgan@clearwater-lantern.com</span>
      </div>
      <div class="contact contact--phone">
        <svg width="22" height="16" viewBox="0 0 22 16" aria-hidden="true"><rect x="1" y="1" width="20" height="14" fill="none" stroke="var(--brand-blue)" stroke-width="2"/><path d="M1,1 L11,9 L21,1 M1,15 L8,7 M21,15 L14,7" fill="none" stroke="var(--brand-blue)" stroke-width="1.6"/></svg>
        <span>518-732-6148</span>
      </div>
    </div>
  </section>
</div>
</body>
</html>
```